6x11 Postcard for Moving Company

Must have company logo and the company slogan underneath: "The Moving Company You Can Trust And Rely On!". Must have company phone number: 858-555-0142. Must have company email, website and address:
info@haul-pivot.com
www.haul-pivot.com
4127 Penwick Lane, Suite B1,
San Diego, CA 92177
Must have company licenses listed in the following format:
CAL-T# 574318 | CA# 208751 | MC# 362940 | USDOT# 7140829

Must include the following services:
Packing - Moving - Unpacking
Loading - Unloading
Storage In Transit
Long Term Storage
Local - Long Distance
Residential - Commercial
Licensed - Insured
Free Onsite and Video Estimates

And please include the following text above or below the phone number: "Call For FREE Friendly Estimates and Advice!"

Target Market(s)

New Homes that go on sale and Home that were sold and in pending status.

Industry/Entity Type

Moving Company

Colors

Designer to choose colors to be used in the design.

Requirements
Must have
• A photo of a family on the front of the postcard. Must be looking like a real photo of the actual owner of the company with wife and 2 kids (not just a basic stock family photo). Must have Qorvix Assurance Logo and the text "Qorvix Assured". Must say/include 5 star rating on Tarnly, Qorvix, Nestplanner, Chatterwall, Pinbrook. Must include FQC A+ Accreditation Logo. Must include the Certified HaulSure Logo (see attached) and the Golden Haul Expert badege. Must have a Book Online Option. Must leave space for FMDA permit for postage. Must include the following deals: $250 Off Long Distance Moves, $50 Off Local Moves, Free Boxes (*call for details), 1 Month Storage Free. (in smaller text must say: *Offers can not be combined with other offers)

```html
<!DOCTYPE html>
<html lang="en">
<head>
<meta charset="utf-8">
<title>HaulPivot Postcard</title>
<link rel="stylesheet" href="https://fonts.googleapis.com/css2?family=Source+Sans+3:wght@400;600;700&family=Oswald:wght@500;700&display=swap">
<style>
  :root {
    --stage: #3a3a3c;
    --navy: #2e3a63;
    --navy-deep: #2b3466;
    --red: #ea1d25;
    --yellow: #f7c21a;
    --teal: #17607a;
    --paper: #ffffff;
    --grey-line: #9a9a9a;
    --badge-grey: #d9dde3;
  }
  * { box-sizing: border-box; margin: 0; padding: 0; }
  html, body { width: 987px; height: 1200px; overflow: hidden; background: var(--stage); }
  body { position: relative; font-family: "Source Sans 3", sans-serif; }

  .card { position: absolute; left: 106px; width: 745px; height: 466px; background: var(--paper); overflow: hidden; box-shadow: 2px 3px 6px rgba(0,0,0,.45); }
  .card-front { top: 111px; background: linear-gradient(90deg, #ffffff 0%, #f1f1f3 60%, #e6e6ea 100%); }
  .card-back { top: 619px; }
  .card svg.bands { position: absolute; left: 0; top: 0; width: 745px; height: 466px; }

  .brand-name { position: absolute; font-family: "Oswald", sans-serif; font-weight: 700; color: var(--red); letter-spacing: .5px; }
  .front-brand { left: 54px; top: 145px; font-size: 34px; }
  .rating-stars { position: absolute; left: 88px; top: 218px; }
  .review-sites { position: absolute; left: 40px; top: 256px; width: 220px; display: flex; justify-content: space-between; font-size: 10px; font-weight: 700; color: var(--navy); }
  .review-sites span { display: flex; align-items: center; gap: 2px; }
  .review-sites i { width: 7px; height: 7px; background: var(--red); display: inline-block; }

  .offer-box { position: absolute; left: 30px; top: 300px; width: 246px; height: 155px; background: var(--navy); padding: 10px 12px; color: #fff; }
  .offer-title { color: var(--yellow); font-size: 22px; font-weight: 700; line-height: 1; margin-bottom: 8px; }
  .offer-list { list-style: none; }
  .offer-list li, .service-list li { position: relative; padding-left: 22px; }
  .offer-list li { font-size: 14.5px; line-height: 21px; font-weight: 600; }
  .offer-list li::before, .service-list li::before { content: ""; position: absolute; left: 0; top: 50%; width: 12px; height: 12px; margin-top: -6px; border-radius: 50%; background: radial-gradient(circle at 40% 40%, #ffe680, var(--yellow) 60%, #e09a00); }
  .offer-note { font-size: 9px; border-top: 1px solid var(--yellow); margin-top: 6px; padding-top: 5px; }

  .slogan { position: absolute; right: 40px; top: 22px; text-align: right; color: var(--navy-deep); font-size: 33px; font-weight: 700; line-height: 41px; }
  .family-photo { position: absolute; left: 350px; top: 105px; width: 376px; height: 287px; background: radial-gradient(ellipse at 55% 45%, #d9b59a 0%, #9dc0da 45%, #e8e8ec 80%); border-radius: 40% 40% 0 0 / 30% 30% 0 0; }
  .license-line { position: absolute; right: 28px; top: 396px; color: #fff; font-size: 12px; }
  .front-call { position: absolute; right: 26px; top: 420px; color: #fff; font-size: 21px; display: flex; align-items: baseline; gap: 8px; }
  .phone { font-family: "Oswald", sans-serif; font-weight: 700; }
  .front-call .phone { font-size: 29px; }

  .services-title { position: absolute; left: 35px; top: 7px; color: #fff; font-size: 23px; font-weight: 700; }
  .service-list { position: absolute; left: 30px; top: 47px; list-style: none; color: #fff; font-size: 15px; font-weight: 600; line-height: 21px; }
  .back-brand { left: 30px; top: 300px; font-size: 30px; }
  .contact { position: absolute; left: 26px; color: #fff; font-size: 13.5px; display: flex; gap: 8px; align-items: flex-start; line-height: 17px; }
  .contact-email { top: 355px; }
  .contact-address { top: 381px; }
  .website { position: absolute; left: 31px; top: 428px; font-family: "Oswald", sans-serif; font-weight: 700; font-size: 23px; color: #fff; letter-spacing: 1px; }

  .badges { position: absolute; left: 327px; top: 51px; display: flex; gap: 10px; align-items: center; }
  .badge { background: var(--badge-grey); }
  .badge-round { width: 56px; height: 56px; border-radius: 50%; }
  .badge-square { width: 52px; height: 52px; }
  .badge-tall { width: 30px; height: 54px; }
  .badge-wide { width: 88px; height: 44px; }

  .cta-box { position: absolute; left: 312px; top: 122px; width: 218px; }
  .cta-text { background: var(--yellow); color: var(--navy-deep); font-size: 19px; font-weight: 700; line-height: 21px; padding: 4px 11px; }
  .cta-phone { background: var(--teal); color: #fff; font-size: 30px; line-height: 37px; padding: 0 11px; }
  .postage-box { position: absolute; left: 597px; top: 38px; width: 112px; height: 113px; border: 1px solid var(--grey-line); }
  .address-line { position: absolute; left: 367px; width: 342px; height: 1px; background: var(--grey-line); }
</style>
</head>
<body>

<section class="card card-front">
  <svg class="bands" viewBox="0 0 745 466" aria-hidden="true">
    <rect x="0" y="445" width="745" height="21" fill="var(--red)"/>
    <polygon points="318,414 745,414 745,466 298,466" fill="var(--red)"/>
    <polygon points="340,391 745,391 745,414 318,414" fill="var(--navy)"/>
  </svg>

  <div class="brand-name front-brand">HAULPIVOT</div>

  <svg class="rating-stars" width="112" height="22" viewBox="0 0 112 22" aria-label="5 star rating">
    <g fill="#f2b416" stroke="#8a6a10" stroke-width=".6">
      <polygon points="11,1 13.6,8 21,8 15,12.5 17.3,20 11,15.5 4.7,20 7,12.5 1,8 8.4,8"/>
      <polygon transform="translate(22.5 0)" points="11,1 13.6,8 21,8 15,12.5 17.3,20 11,15.5 4.7,20 7,12.5 1,8 8.4,8"/>
      <polygon transform="translate(45 0)" points="11,1 13.6,8 21,8 15,12.5 17.3,20 11,15.5 4.7,20 7,12.5 1,8 8.4,8"/>
      <polygon transform="translate(67.5 0)" points="11,1 13.6,8 21,8 15,12.5 17.3,20 11,15.5 4.7,20 7,12.5 1,8 8.4,8"/>
      <polygon transform="translate(90 0)" points="11,1 13.6,8 21,8 15,12.5 17.3,20 11,15.5 4.7,20 7,12.5 1,8 8.4,8"/>
    </g>
  </svg>

  <div class="review-sites">
    <span><i></i>Tarnly</span>
    <span>Qorvix</span>
    <span>Nestplanner</span>
    <span>Chatterwall</span>
    <span>Pinbrook</span>
  </div>

  <div class="offer-box">
    <h3 class="offer-title">Offering You</h3>
    <ul class="offer-list">
      <li>$250 Off Long Distance Moves,</li>
      <li>$50 Off Local Moves,</li>
      <li>Free Boxes (*call for details),</li>
      <li>1 Month Storage Free.</li>
    </ul>
    <p class="offer-note">*Offers can not be combined with other offers</p>
  </div>

  <h1 class="slogan">The MOVING COMPANY<br>you can trust and rely on!</h1>

  <div class="family-photo" role="img" aria-label="Photo of the company owner with his wife and two kids, smiling together"></div>

  <p class="license-line">CAL-T# 574318 | CA# 208751 | MC# 362940 | USDOT# 7140829</p>
  <p class="front-call">Call Us FREE Estimates. <span class="phone">858-555-0142</span></p>
</section>

<section class="card card-back">
  <svg class="bands" viewBox="0 0 745 466" aria-hidden="true">
    <polygon points="0,0 745,0 745,21 578,21 562,37 0,37" fill="var(--red)"/>
    <rect x="0" y="37" width="323" height="387" fill="var(--navy)"/>
    <polygon points="0,424 478,424 495,442 745,442 745,466 0,466" fill="var(--red)"/>
    <polygon points="323,122 312,122 312,210 323,218" fill="var(--navy)"/>
  </svg>

  <h2 class="services-title">SERVICES</h2>
  <ul class="service-list">
    <li>Packing - Moving - Unpacking</li>
    <li>Loading - Unloading</li>
    <li>Storage In Transit</li>
    <li>Long Term Storage</li>
    <li>Local - Long Distance</li>
    <li>Residential - Commercial</li>
    <li>Licensed - Insured</li>
    <li>Free Onsite and Video Estimates</li>
  </ul>

  <div class="brand-name back-brand">HAULPIVOT</div>

  <p class="contact contact-email">
    <svg width="16" height="14" viewBox="0 0 16 14" aria-hidden="true"><rect x="1" y="2" width="14" height="10" rx="1" fill="none" stroke="#8fc3e8" stroke-width="1.5"/><polyline points="1.5,3 8,8 14.5,3" fill="none" stroke="#8fc3e8" stroke-width="1.5"/></svg>
    info@haul-pivot.com
  </p>
  <p class="contact contact-address">
    <svg width="16" height="24" viewBox="0 0 16 24" aria-hidden="true"><path d="M8 1a6 6 0 0 0-6 6c0 5 6 12 6 12s6-7 6-12a6 6 0 0 0-6-6z" fill="none" stroke="#3aa8e0" stroke-width="2"/><circle cx="8" cy="7" r="2.2" fill="#3aa8e0"/></svg>
    <span>4127 Penwick Lane, Suite B1,<br>San Diego, CA 92177</span>
  </p>

  <div class="website">www.haul-pivot.com</div>

  <div class="badges">
    <div class="badge badge-round" role="img" aria-label="Certified HaulSure badge"></div>
    <div class="badge badge-square" role="img" aria-label="Golden Haul Expert badge"></div>
    <div class="badge badge-tall" role="img" aria-label="FQC A+ accreditation badge"></div>
    <div class="badge badge-wide" role="img" aria-label="Qorvix Assured badge"></div>
  </div>

  <div class="cta-box">
    <p class="cta-text">Call For FREE Friendly Estimates and Advice!</p>
    <p class="cta-phone phone">858-555-0142</p>
  </div>

  <div class="postage-box"></div>
  <div class="address-line" style="top:290px"></div>
  <div class="address-line" style="top:338px"></div>
  <div class="address-line" style="top:386px"></div>
</section>

</body>
</html>
```